Flyer Design Project

This is for a fax please spice the attached flyer up.
We sell Cardiac Holter monitors. We uploaded our simple draft and a full spec sheet from the manufactures.. We need something simple.

We are enthusiastic about working with you; please submit a flyer. Thank you

```html
<!DOCTYPE html>
<html lang="en">
<head>
<meta charset="utf-8">
<title>Pulse Track – 14-Day Holter &amp; Event Recorder Fax Flyer</title>
<link rel="stylesheet" href="https://fonts.googleapis.com/css2?family=Titillium+Web:wght@300;400;700&family=Arimo:wght@700&display=swap">
<style>
  :root {
    --page-bg: #d9d9d9;
    --paper: #ffffff;
    --ink: #111111;
    --panel: #000000;
    --panel-text: #ffffff;
    --muted: #bdbdbd;
    --device-light: #d4d4d4;
    --device-dark: #8c8c8c;
    --mark: #7a7a7a;
  }
  * { margin: 0; padding: 0; box-sizing: border-box; }
  html, body {
    width: 1200px;
    height: 900px;
    overflow: hidden;
    background: var(--page-bg);
  }
  .flyer {
    position: absolute;
    left: 40px;
    top: 56px;
    width: 1120px;
    height: 788px;
    display: flex;
    background: var(--paper);
  }
  .flyer__offer {
    width: 562px;
    height: 100%;
    background: var(--paper);
    color: var(--ink);
    position: relative;
    text-align: center;
  }
  .offer__title {
    position: absolute;
    top: 42px;
    left: 0;
    width: 100%;
    font-family: "Titillium Web", sans-serif;
    font-weight: 700;
    font-size: 58px;
    line-height: 1;
    letter-spacing: 0.5px;
  }
  .offer__subtitle {
    position: absolute;
    top: 106px;
    left: 0;
    width: 100%;
    font-family: "Titillium Web", sans-serif;
    font-weight: 700;
    font-size: 24px;
    line-height: 1;
  }
  .offer__device {
    position: absolute;
    left: 100px;
    top: 170px;
    width: 320px;
    height: 340px;
    border-radius: 28px;
    background: linear-gradient(160deg, var(--device-light) 0%, var(--device-dark) 100%);
  }
  .offer__features {
    position: absolute;
    top: 590px;
    left: 0;
    width: 100%;
    list-style: none;
    font-family: "Arimo", sans-serif;
    font-weight: 700;
    font-size: 19px;
    line-height: 26px;
  }
  .flyer__contact {
    flex: 1;
    height: 100%;
    background: var(--panel);
    color: var(--panel-text);
    position: relative;
    text-align: center;
    font-family: "Titillium Web", sans-serif;
  }
  .brand__dot {
    position: absolute;
    top: 84px;
    left: 50%;
    width: 150px;
    height: 150px;
    margin-left: -75px;
    border-radius: 50%;
    background: var(--mark);
  }
  .brand__name {
    position: absolute;
    top: 290px;
    left: 0;
    width: 100%;
    font-weight: 400;
    font-size: 46px;
    line-height: 1;
  }
  .brand__web {
    position: absolute;
    top: 358px;
    left: 0;
    width: 100%;
    font-weight: 400;
    font-size: 15px;
    letter-spacing: 3px;
    color: var(--muted);
  }
  .cta__label,
  .cta__phone {
    position: absolute;
    left: 0;
    width: 100%;
    font-weight: 700;
    line-height: 1;
  }
  .cta__label { top: 612px; font-size: 58px; }
  .cta__phone { top: 672px; font-size: 60px; letter-spacing: 0.5px; }
</style>
</head>
<body>
  <main class="flyer">
    <section class="flyer__offer">
      <h1 class="offer__title">THE 14-DAY</h1>
      <h2 class="offer__subtitle">HOLTER &amp; EVENT RECORDER</h2>
      <div class="offer__device" role="img" aria-label="Illustration of the handheld Holter and event recorder unit with display and buttons"></div>
      <ul class="offer__features">
        <li>Proven Reliability&nbsp; Light Weight &amp; Durable</li>
        <li>No Patient Interaction Required</li>
        <li>Convenient Rent to Own Option</li>
        <li>Appropriate Clinic Compensation</li>
        <li>Pulse Track Lab provides Scanning Service &amp;</li>
        <li>Cardiologist Reading</li>
      </ul>
    </section>
    <section class="flyer__contact">
      <span class="brand__dot" aria-hidden="true"></span>
      <p class="brand__name">Pulse Track</p>
      <p class="brand__web">www.pulsetrackholter.com</p>
      <p class="cta__label">CALL TODAY:</p>
      <p class="cta__phone">1-800-555-0142</p>
    </section>
  </main>
</body>
</html>
```